UK landscaping company needs website

We, Brindle Landscapes need a website design for a company based in Surrey, UK. The design should be bold and playful. We have three main areas of work driveways, paving and fencing. It shouldn't be too heavy in text and concentrate on the pictures from previous jobs we've completed. You may use stock images for the design, these can be changed if you are successful. Please don’t just copy the flyer it is just there to provide content.
We have a logo design which we would also like editing slightly.
Here are some of my local competitors
https://www.vexmoorlandscapes.co.uk/

https://www.twinreedgardendesign.com/

https://quarnelllandscapes.co.uk/

Industry/Entity Type

Landscaping

Coding

Coded - Design and coding required

Number of Pages Required

3 page

Font styles to use
Sans Serif

Requirements
Must have
• Pictures of my previous jobs.
Must be mobile friendly
Easy to navigate
Nice to have
• Try to use different colours. It would be good to have some designs that aren’t just black and green.
I’d like some curves in the design.
Should not have
• We install hard landscaping. Think more building/construction and less plants and cutting grass.

```html
<!DOCTYPE html>
<html lang="en">
<head>
<meta charset="utf-8">
<title>Brindle Landscapes</title>
<link rel="stylesheet" href="https://fonts.googleapis.com/css2?family=Montserrat:wght@500;600;700&family=Raleway:wght@400;500;600&display=swap">
<style>
:root{
  --green:#58b52b;
  --green-dark:#4ea225;
  --black:#0d0b0c;
  --ink:#222;
  --grey-bg:#f4f4f4;
  --white:#fff;
  --muted:#777;
}
*{box-sizing:border-box;margin:0;padding:0}
html,body{width:1200px;height:4545px;overflow:hidden}
body{font-family:"Raleway",sans-serif;color:var(--ink);background:var(--white);position:relative}
.abs{position:absolute}
h1,h2,h3{font-family:"Montserrat",sans-serif;font-weight:600}
.photo{position:absolute}

/* top bar */
.topbar{left:0;top:0;width:1200px;height:74px;background:var(--black)}
.brand{left:90px;top:12px;display:flex;align-items:center;gap:10px;color:var(--white);font-family:"Montserrat",sans-serif;font-weight:700;font-size:30px;letter-spacing:1px}
.brand-dot{width:14px;height:14px;background:var(--green);border-radius:50%}
.callbar{left:785px;top:0;width:415px;height:74px;background:var(--green);color:var(--white);font-family:"Montserrat",sans-serif;font-weight:600;font-size:18px;display:flex;align-items:center;padding-left:27px}
.callbar b{font-size:21px;font-weight:600;margin-left:4px}

/* nav */
.nav{left:0;top:74px;width:1200px;height:62px;background:var(--white)}
.nav a{position:absolute;top:22px;font-size:14.5px;color:#333;text-decoration:none}
.nav a.active{color:var(--green)}
.login{display:flex;align-items:center;gap:6px}

/* hero */
.hero-photo{left:0;top:136px;width:992px;height:556px;background:linear-gradient(135deg,#b9aa9b 0%,#d9c4b1 35%,#c8b3a2 60%,#a99687 100%)}
.hero-photo::after{content:"";position:absolute;left:290px;top:0;width:380px;height:130px;background:linear-gradient(160deg,#3c96cc,#2a7fb8);border-radius:0 0 60px 60px;opacity:.9}
.hero-box{left:520px;top:252px;width:587px;height:325px;background:var(--green);color:var(--white);padding:42px 50px}
.hero-box h1{font-size:64px;line-height:66px;font-weight:500}
.hero-box p{font-size:15px;line-height:25px;margin-top:16px;width:460px}
.btn-dark{position:absolute;right:0;bottom:0;width:233px;height:57px;background:var(--black);border:2px solid var(--black);color:var(--white);font-size:17px;display:flex;align-items:center}
.btn-dark span{flex:1;text-align:center;padding-right:10px}
.btn-dark i{width:52px;height:100%;background:var(--green);display:flex;align-items:center;justify-content:center}

/* services */
.services{left:0;top:692px;width:1200px;height:600px;background:var(--grey-bg)}
.sec-title{text-align:center;font-size:40px;font-weight:500;color:#1a1a1a}
.services .sec-title{position:absolute;top:80px;width:100%}
.card{position:absolute;top:155px;width:260px;height:270px;background:var(--white);box-shadow:0 3px 10px rgba(0,0,0,.08)}
.card .photo{left:0;top:0;width:260px;height:185px}
.card h3{position:absolute;top:215px;width:100%;text-align:center;font-family:"Raleway",sans-serif;font-weight:500;font-size:17px;color:#222}
.btn-green{position:absolute;left:470px;top:457px;width:259px;height:56px;background:var(--green);border:2px solid var(--black);color:var(--white);font-size:17px;display:flex;align-items:center}
.btn-green span{flex:1;text-align:center}
.btn-green i{width:52px;height:100%;background:var(--black);display:flex;align-items:center;justify-content:center}

/* about */
.about{left:0;top:1292px;width:600px;height:591px;background:var(--green);color:var(--white);padding:70px 90px}
.about h2,.who h2{font-size:40px;font-weight:500;margin-bottom:18px}
.about p,.who p{font-size:15px;line-height:36px;text-align:justify;margin-bottom:8px}
.about-photo{left:600px;top:1292px;width:600px;height:591px;background:linear-gradient(180deg,#8c8f86 0%,#b7b2a8 30%,#cdbcb0 65%,#7fa25c 100%)}

/* who */
.who-photo{left:0;top:1883px;width:600px;height:487px;background:linear-gradient(160deg,#9a7b5e 0%,#5e6b3c 22%,#7e7e80 40%,#9b9b9e 75%,#cfcfcf 100%)}
.play{left:260px;top:2090px;width:62px;height:62px;border-radius:50%;background:var(--black);display:flex;align-items:center;justify-content:center}
.who{left:600px;top:1883px;width:600px;height:487px;background:var(--black);color:var(--white);padding:100px 52px 0 52px}

/* testimonials */
.testi{left:0;top:2370px;width:1200px;height:410px;background:var(--green);color:var(--white);text-align:center}
.testi h2{position:absolute;top:78px;width:100%;font-size:40px;font-weight:500}
.testi blockquote{position:absolute;left:155px;top:150px;width:890px;font-size:14px;line-height:31px}
.testi .name{position:absolute;top:262px;width:100%;font-family:"Montserrat",sans-serif;font-weight:500;font-size:16px}
.dots{position:absolute;left:580px;top:317px;display:flex;gap:9px}
.dots i{width:5px;height:5px;border-radius:50%;background:var(--white)}
.arrow{position:absolute;top:182px}

/* projects */
.projects-title{left:0;top:2780px;width:400px;height:284px;background:var(--white);padding:60px 90px}
.projects-title h2{font-size:40px;line-height:54px;font-weight:600;color:#1a1a1a}

/* features */
.feature{position:absolute;top:3436px;width:210px;text-align:center}
.feature svg{display:block;margin:0 auto}
.feature .icon{position:absolute;left:75px;top:70px;width:60px;height:60px;border-radius:50%;background:#e3f2da}
.feature h3{margin-top:32px;font-size:27px;font-weight:500;color:#222}

/* contact */
.contact{left:0;top:3773px;width:1200px;height:568px;background:linear-gradient(180deg,#2a2a2a 0%,#1c1c1c 45%,#3a302a 100%);color:var(--white)}
.contact h2{position:absolute;top:85px;width:100%;text-align:center;font-size:40px;font-weight:500}
.contact .sub{position:absolute;top:150px;width:100%;text-align:center;font-size:16px}
.field{position:absolute;background:var(--white);border:1px solid #ccc;color:#888;font-size:13.5px;padding:13px 15px}
.send{position:absolute;left:187px;top:457px;width:826px;height:44px;background:var(--green);color:var(--white);font-family:"Montserrat",sans-serif;font-weight:500;font-size:17px;display:flex;align-items:center;justify-content:center}

/* footer */
.footer{left:0;top:4341px;width:1200px;height:204px;background:var(--black);color:var(--white)}
.finfo{position:absolute;top:30px;display:flex;gap:20px}
.finfo .ic{width:42px;height:42px;border:1px solid var(--white);display:flex;align-items:center;justify-content:center}
.finfo div p{font-size:12.5px;line-height:23px}
.finfo div p b{font-family:"Montserrat",sans-serif;font-weight:600;font-size:13.5px}
.socials{position:absolute;left:526px;top:136px;display:flex;gap:9px}
.socials i{width:42px;height:42px;border:2px solid var(--white);border-radius:50%;display:block}
.copy{position:absolute;top:185px;width:100%;text-align:center;font-size:10.5px}
</style>
</head>
<body>

<header>
  <div class="abs topbar"></div>
  <div class="abs brand"><span>BRINDLE</span><span class="brand-dot"></span></div>
  <div class="abs callbar">Call Us Now : <b>+07700 900 481</b></div>
  <nav class="abs nav">
    <a class="active" style="left:88px">Home</a>
    <a style="left:171px">About Us</a>
    <a style="left:275px">Services</a>
    <a style="left:374px">Who We Are</a>
    <a style="left:505px">Projects</a>
    <a style="left:600px">Blog</a>
    <a style="left:672px">Gallery</a>
    <a style="left:760px">Contact us</a>
    <a class="login" style="left:1045px"><svg width="12" height="13" viewBox="0 0 12 13"><circle cx="6" cy="3.5" r="3" fill="#58b52b"/><path d="M0 13c0-4 2.5-6 6-6s6 2 6 6z" fill="#58b52b"/></svg>Log In</a>
  </nav>
</header>

<section>
  <div class="photo hero-photo" role="img" aria-label="Sandstone patio around a swimming pool"></div>
  <div class="abs hero-box">
    <h1>Brindle Landscapes</h1>
    <p>Lorem ipsum dolor sit amet, consectetur adipiscing elit, sed do eiusmod tempor incididunt</p>
    <div class="btn-dark"><span>Get Started</span><i><svg width="10" height="14" viewBox="0 0 10 14"><path d="M2 1l6 6-6 6" stroke="#fff" stroke-width="1.8" fill="none"/></svg></i></div>
  </div>
</section>

<section class="abs services">
  <h2 class="sec-title">Services</h2>
  <div class="card" style="left:180px"><div class="photo" role="img" aria-label="Grey stone steps on a driveway" style="background:linear-gradient(160deg,#7a4a36 0%,#a9a9a6 45%,#c8c6c1 80%,#9b6b4b 100%)"></div><h3>Work Driveways</h3></div>
  <div class="card" style="left:470px"><div class="photo" role="img" aria-label="Garden with newly laid paving and lawn" style="background:linear-gradient(180deg,#4f6a3c 0%,#7a8a5a 45%,#5ea03b 70%,#b98e7c 100%)"></div><h3>Paving</h3></div>
  <div class="card" style="left:759px"><div class="photo" role="img" aria-label="New timber panel fencing beside a lawn" style="background:linear-gradient(180deg,#6f8a4c 0%,#8e7452 35%,#a08562 70%,#6aa23d 100%)"></div><h3>Fencing</h3></div>
  <div class="btn-green"><span>Learn More</span><i><svg width="10" height="14" viewBox="0 0 10 14"><path d="M2 1l6 6-6 6" stroke="#fff" stroke-width="1.8" fill="none"/></svg></i></div>
</section>

<section>
  <div class="abs about">
    <h2>About Us</h2>
    <p>Lorem ipsum dolor sit amet, consectetur adipiscing elit, sed do eiusmod tempor incididunt ut labore et dolore magna aliqua. Ut enim ad minim veniam, quis nostrud exercitation lamco laboris nisi ut aliquip ex ea commodo consequat. Duis aute irure dolor in reprehenderit in voluptate velit esse cillum dolore eu fugiat nulla pariatur.</p>
    <p>Lorem ipsum dolor sit amet, consectetur adipiscing elit, sed do eiusmod tempor incididunt ut labore et dolore magna aliqua. Lorem ipsum dolor sit amet, consectetur adipiscing elit, sed do eiusmod tempor incididunt ut labore et dolore magna aliqua.</p>
  </div>
  <div class="photo about-photo" role="img" aria-label="Circular sandstone patio outside a summer house"></div>
</section>

<section>
  <div class="photo who-photo" role="img" aria-label="Grey block paving driveway with drainage channel"></div>
  <div class="abs play"><svg width="16" height="18" viewBox="0 0 16 18"><path d="M2 1l13 8-13 8z" fill="#58b52b"/></svg></div>
  <div class="abs who">
    <h2>Who We Are</h2>
    <p>Lorem ipsum dolor sit amet, consectetur adipiscing elit, sed do eiusmod tempor incididunt ut labore et dolore magna aliqua. Ut enim ad minim veniam, quis nostrud exercitation lamco laboris nisi ut aliquip ex ea commodo consequat. Duis aute irure dolor in reprehenderit in voluptate velit esse cillum dolore eu fugiat nulla pariatur.</p>
  </div>
</section>

<section class="abs testi">
  <h2>Testimonials</h2>
  <svg class="arrow" style="left:90px" width="12" height="22" viewBox="0 0 12 22"><path d="M10 2L2 11l8 9" stroke="#fff" stroke-width="2.5" fill="none"/></svg>
  <blockquote>"Lorem ipsum dolor sit amet, consectetur adipiscing elit, sed do eiusmod tempor incididunt ut labore et dolore magna aliqua. Ut enim ad minim veniam, quis nostrud exercitation ullamco laboris nisi ut aliquip ex ea commodo consequat. Duis aute irure dolor in reprehenderit in voluptate velit esse cillum dolore eu fugiat nulla pariatur. "</blockquote>
  <p class="name">Ella Marsh.</p>
  <div class="dots"><i></i><i></i><i></i></div>
  <svg class="arrow" style="left:1096px" width="12" height="22" viewBox="0 0 12 22"><path d="M2 2l8 9-8 9" stroke="#fff" stroke-width="2.5" fill="none"/></svg>
</section>

<section>
  <div class="abs projects-title"><h2>Our<br>Latest<br>Projects</h2></div>
  <div class="photo" role="img" aria-label="Narrow garden with grey paving and artificial lawn" style="left:400px;top:2780px;width:400px;height:284px;background:linear-gradient(160deg,#6b5f52 0%,#5fa53c 35%,#8d8a86 65%,#9b6a4a 100%)"></div>
  <div class="photo" role="img" aria-label="Wet red and grey block paving" style="left:800px;top:2780px;width:400px;height:284px;background:linear-gradient(170deg,#8a4a3e 0%,#7b6c78 45%,#5a5f74 100%)"></div>
  <div class="photo" role="img" aria-label="Large grey paving slabs by a lawn" style="left:0;top:3064px;width:400px;height:284px;background:linear-gradient(120deg,#5f8a3a 0%,#a8adaf 40%,#8e9396 100%)"></div>
  <div class="photo" role="img" aria-label="Pergola with trellis over a grey patio" style="left:400px;top:3064px;width:400px;height:284px;background:linear-gradient(180deg,#8a7b68 0%,#9b8f80 45%,#c7c5c3 75%,#4f7a35 100%)"></div>
  <div class="photo" role="img" aria-label="Raised timber deck and lawn beside a house" style="left:800px;top:3064px;width:400px;height:284px;background:linear-gradient(180deg,#b7a383 0%,#c9b18b 40%,#4e8a2f 70%,#a88b62 100%)"></div>
</section>

<section>
  <div class="feature" style="left:154px">
    <svg width="210" height="210" viewBox="0 0 210 210"><circle cx="105" cy="105" r="99" fill="none" stroke="#58b52b" stroke-width="8" stroke-dasharray="560 62" transform="rotate(-20 105 105)"/></svg>
    <span class="icon" role="img" aria-label="Award rosette icon"></span>
    <h3>Quality</h3>
  </div>
  <div class="feature" style="left:495px">
    <svg width="210" height="210" viewBox="0 0 210 210"><circle cx="105" cy="105" r="99" fill="none" stroke="#58b52b" stroke-width="8" stroke-dasharray="560 62" transform="rotate(-20 105 105)"/></svg>
    <span class="icon" role="img" aria-label="Handshake and team icon"></span>
    <h3>Work Experience</h3>
  </div>
  <div class="feature" style="left:836px">
    <svg width="210" height="210" viewBox="0 0 210 210"><circle cx="105" cy="105" r="99" fill="none" stroke="#58b52b" stroke-width="8" stroke-dasharray="560 62" transform="rotate(-20 105 105)"/></svg>
    <span class="icon" role="img" aria-label="Hand holding money icon"></span>
    <h3>Cost Effective</h3>
  </div>
</section>

<section class="abs contact" role="img" aria-label="Dusk garden scene behind the contact form">
  <h2>Contact Us</h2>
  <p class="sub">Call or Message Us for a Free Quote!</p>
  <div class="field" style="left:187px;top:200px;width:404px;height:44px">First Name</div>
  <div class="field" style="left:608px;top:200px;width:405px;height:44px">Last Name</div>
  <div class="field" style="left:187px;top:262px;width:404px;height:44px">Email</div>
  <div class="field" style="left:608px;top:262px;width:405px;height:44px">Phone No</div>
  <div class="field" style="left:187px;top:325px;width:826px;height:113px">Message</div>
  <div class="send">Send</div>
</section>

<footer class="abs footer">
  <div class="finfo" style="left:187px">
    <span class="ic"><svg width="16" height="16" viewBox="0 0 16 16"><path d="M3 1l3 3-2 2c1 2 3 4 5 5l2-2 3 3-2 3C7 15 1 9 1 3z" fill="#fff"/></svg></span>
    <div><p>Call Us :</p><p><b>07700 900 481</b></p></div>
  </div>
  <div class="finfo" style="left:502px">
    <span class="ic"><svg width="18" height="14" viewBox="0 0 18 14"><rect x="1" y="1" width="16" height="12" fill="#fff"/><path d="M1 1l8 7 8-7" stroke="#0d0b0c" stroke-width="1.5" fill="none"/></svg></span>
    <div><p>Email Us :</p><p><b>info@brindle-landscapes.com</b></p></div>
  </div>
  <div class="finfo" style="left:817px">
    <span class="ic"><svg width="16" height="16" viewBox="0 0 16 16"><path d="M3 1l3 3-2 2c1 2 3 4 5 5l2-2 3 3-2 3C7 15 1 9 1 3z" fill="#fff"/></svg></span>
    <div><p>Address :</p><p><b>27 Brindle Yard</b><br><b>Dorking, Surrey, UK</b></p></div>
  </div>
  <div class="socials"><i></i><i></i><i></i></div>
  <p class="copy">© 2020 Copyrights The Company Name.All Rights Reserved</p>
</footer>

</body>
</html>
```